Oversized Post Card for Busines Owners 1st 2nd and 3rd prizes

Create a professional, fresh and polished oversized post card for law firm specializing in Business Law, Succession Planning, and Employment Law

Use any picture(s) of your choice (mine or ones you recommend), logo, headshot and company info

www.morvenashcroftlegal.example

Brookhaven Office - 4800 Tillman Road, Suite 1400, Charlotte, NC 28219
Whitcombe Office - 13540 Quarry Lane, Suite 300, Charlotte, NC 28269

Phone (704) 555-0187

Use this card for a Free Consultation

Target Market(s)

Business Owners (of small businesses)

Industry/Entity Type

Business

Font styles to use
Serif
Sans Serif

Requirements
Must have
• Company name, logo and contact info
• Serving business owners with legal guidance
• Business Law, Succession Planning & Wealth Transfers
• www.morvenashcroftlegal.example
• Brookhaven Office - 4800 Tillman Road, Suite 1400, Charlotte, NC 28219
• Whitcombe Office - 13540 Quarry Lane, Suite 300, Charlotte, NC 28269
• Phone (704) 555-0187
• Use this card for a Free Consultation
Nice to have
• pictures (yours or mine) - you choose; headshot picture

```html
<!DOCTYPE html>
<html lang="en">
<head>
<meta charset="utf-8">
<title>Morven Ashcroft Law – Oversized Postcard</title>
<link rel="stylesheet" href="https://fonts.googleapis.com/css2?family=Marcellus&family=Raleway:wght@300&family=Lato:wght@400;700&display=swap">
<style>
  :root{
    --navy:#063d5c;
    --blue:#1b6a8d;
    --teal:#1289b0;
    --sky:#2ba3cb;
    --band:#0e88b0;
    --ink:#333c44;
    --panel:#f0f1f2;
    --paper:#ffffff;
    --page:#e8e8e8;
  }
  *{box-sizing:border-box;margin:0;padding:0}
  html,body{width:965px;height:1200px;overflow:hidden;background:var(--page)}
  .card{position:absolute;left:42px;width:863px;height:560px;transform:scale(1.0197);transform-origin:0 0;overflow:hidden;background:var(--paper);box-shadow:0 2px 8px rgba(0,0,0,.25)}
  .card--front{top:18px}
  .card--back{top:609px}
  .card svg.shapes{position:absolute;inset:0}
  .abs{position:absolute}
  .serif{font-family:"Marcellus",Georgia,serif}
  .sans{font-family:"Lato",Arial,sans-serif}

  /* front */
  .headline{left:0;width:487px;top:42px;text-align:center;color:#fff;font-size:30px;letter-spacing:2px;line-height:38px}
  .services{left:30px;top:188px;list-style:none;font-family:"Raleway",Arial,sans-serif;font-weight:300;color:#fff;font-size:30px;line-height:38px}
  .services li{display:flex;align-items:center;gap:12px}
  .services li::before{content:"";width:16px;height:16px;border-radius:50%;background:#fff;
    background-image:linear-gradient(45deg,transparent 45%,var(--navy) 45%,var(--navy) 58%,transparent 58%),linear-gradient(-45deg,transparent 45%,var(--navy) 45%,var(--navy) 58%,transparent 58%);
    background-size:100% 50%;background-position:0 0,0 100%;background-repeat:no-repeat}
  .tagline{left:0;width:430px;top:372px;text-align:center;color:#fff;font-size:18px;line-height:24px}
  .badge-text{left:405px;top:412px;width:154px;text-align:center;color:#fff;font-size:16px;line-height:20px;letter-spacing:.3px}
  .brand{display:flex;align-items:center;gap:14px}
  .brand__mark{width:66px;height:66px;border-radius:50%;background:var(--teal);flex:none}
  .brand__name{color:var(--teal);line-height:1.05;letter-spacing:2px}
  .brand--front{left:24px;top:468px}
  .brand--front .brand__name{font-size:30px}
  .brand__sub{display:block;font-size:14px;letter-spacing:1.5px;text-align:center}
  .contact{color:#fff;text-align:center}
  .contact__phone{display:flex;align-items:center;justify-content:center;gap:8px}
  .contact--front{left:560px;width:303px;top:482px}
  .contact--front .contact__phone{font-size:22px}
  .contact--front .contact__url{font-size:18.5px;margin-top:6px}

  /* back */
  .brand--back{left:60px;top:36px;flex-direction:column;gap:10px}
  .brand--back .brand__mark{width:80px;height:80px}
  .brand--back .brand__name{font-size:25px;text-align:center}
  .practice{left:22px;top:216px;color:#fff;font-size:27px;letter-spacing:1.6px}
  .motto{left:33px;top:288px;color:var(--teal);font-size:17px;letter-spacing:1.4px}
  .headshot{left:14px;top:327px;width:107px;height:132px;background:linear-gradient(160deg,#c9b07a,#6b5a45 55%,#2a2c33)}
  .bio{left:135px;top:324px;width:297px;color:var(--ink);font-size:12.4px;line-height:15.5px;text-align:justify;hyphens:auto}
  .signature{left:135px;top:440px;width:130px;height:26px;background:linear-gradient(90deg,rgba(18,137,176,.25),rgba(18,137,176,.08))}
  .contact--back{left:0;width:450px;top:492px}
  .contact--back .contact__phone{font-size:19px}
  .contact--back .contact__url{font-size:18.5px;margin-top:4px}
  .office{top:30px;width:140px;color:#222;font-size:11px;line-height:15px}
  .office__name{display:flex;align-items:center;gap:6px;color:var(--teal);font-size:12.5px;font-weight:700;margin-bottom:2px;margin-left:-14px}
  .office--one{left:474px}
  .office--two{left:619px}
  .stamp{left:747px;top:29px;width:93px;height:68px;border:1.5px solid #9aa3a9}
  .address-line{left:531px;width:309px;height:0;border-top:1.2px solid #8d959b}
</style>
</head>
<body>

<section class="card card--front" aria-label="Postcard front">
  <svg class="shapes" viewBox="0 0 863 560" width="863" height="560">
    <defs>
      <linearGradient id="sprout" x1="0" y1="0" x2="0" y2="1">
        <stop offset="0" stop-color="#6f8f3c"/>
        <stop offset=".5" stop-color="#9a8a55"/>
        <stop offset="1" stop-color="#7b5a3d"/>
      </linearGradient>
    </defs>
    <rect width="863" height="560" fill="var(--blue)"/>
    <path d="M560 0 C470 90 395 300 462 452 L863 452 V0 Z" fill="none" stroke="var(--sky)" stroke-width="6"/>
    <path d="M575 0 C485 90 415 300 478 450 L863 450 V0 Z" fill="url(#sprout)" role="img" aria-label="Photo of a young plant growing from a glass jar filled with coins"/>
    <rect x="0" y="166" width="487" height="152" fill="var(--navy)"/>
    <rect x="0" y="440" width="420" height="6" fill="var(--sky)"/>
    <rect x="0" y="448" width="863" height="112" fill="var(--paper)"/>
    <path d="M555 456 H863 V560 H600 C570 520 558 490 555 456 Z" fill="#166d93"/>
    <path d="M520 520 C545 540 570 552 592 560 H578 C555 550 532 538 512 525 Z" fill="var(--sky)"/>
    <circle cx="482" cy="443" r="77" fill="var(--teal)" stroke="#fff" stroke-width="4"/>
  </svg>

  <h1 class="abs headline serif">SERVING BUSINESS OWNERS<br>WITH LEGAL GUIDANCE</h1>
  <ul class="abs services">
    <li>Business Law</li>
    <li>Succession Planning</li>
    <li>Wealth Transfers</li>
  </ul>
  <p class="abs tagline sans">Let the team at Morven Ashcroft Law, PLLC put our experience to work for you!</p>
  <p class="abs badge-text sans">USE THIS CARD FOR A FREE CONSULTATION</p>

  <div class="abs brand brand--front">
    <span class="brand__mark"></span>
    <span class="brand__name serif">MORVEN ASHCROFT<span class="brand__sub">LAW, PLLC</span></span>
  </div>

  <div class="abs contact contact--front sans">
    <div class="contact__phone">
      <svg width="20" height="20" viewBox="0 0 24 24" aria-hidden="true"><circle cx="12" cy="12" r="10.5" fill="none" stroke="#fff" stroke-width="1.8"/><path d="M8.6 6.8l1.7 2.4-1 1.4c.7 1.5 1.8 2.6 3.3 3.3l1.4-1 2.4 1.7-.6 2c-4.6-.3-8.6-4.3-8.9-8.9z" fill="#fff"/></svg>
      (704) 555-0187
    </div>
    <div class="contact__url">www.morvenashcroftlegal.example</div>
  </div>
</section>

<section class="card card--back" aria-label="Postcard back">
  <svg class="shapes" viewBox="0 0 863 560" width="863" height="560">
    <rect width="863" height="560" fill="var(--paper)"/>
    <path d="M0 270 H470 C468 350 458 420 448 480 H0 Z" fill="var(--panel)"/>
    <path d="M390 0 C440 80 470 170 470 260 C470 350 458 420 440 490" fill="none" stroke="#0c5f86" stroke-width="12"/>
    <path d="M0 480 H452 L440 560 H0 Z" fill="var(--band)"/>
    <path d="M466 180 L490 193 H466 Z" fill="#04293e"/>
    <rect x="0" y="193" width="490" height="77" fill="var(--navy)"/>
  </svg>

  <div class="abs brand brand--back">
    <span class="brand__mark"></span>
    <span class="brand__name serif">MORVEN ASHCROFT<span class="brand__sub">LAW, PLLC</span></span>
  </div>

  <h2 class="abs practice serif">ESTATE PLANNING &amp; PROBATE</h2>
  <h3 class="abs motto serif">BIG THINGS START FROM LITTLE IDEAS</h3>
  <div class="abs headshot" role="img" aria-label="Headshot of attorney Morven Ashcroft"></div>
  <p class="abs bio sans">As a Trusts and Estates Attorney, Morven Ashcroft advises clients regarding estate planning, special needs planning, guardianships, probate, estate administration, estate disputes, trust administration, trust and fiduciary disputes, estate tax, income tax, gift tax, succession planning, and other business law matters.</p>
  <div class="abs signature" role="img" aria-label="Handwritten signature of Morven Ashcroft"></div>

  <div class="abs contact contact--back sans">
    <div class="contact__phone">
      <svg width="18" height="18" viewBox="0 0 24 24" aria-hidden="true"><circle cx="12" cy="12" r="10.5" fill="none" stroke="#fff" stroke-width="1.8"/><path d="M8.6 6.8l1.7 2.4-1 1.4c.7 1.5 1.8 2.6 3.3 3.3l1.4-1 2.4 1.7-.6 2c-4.6-.3-8.6-4.3-8.9-8.9z" fill="#fff"/></svg>
      (704) 555-0187
    </div>
    <div class="contact__url">www.morvenashcroftlegal.example</div>
  </div>

  <address class="abs office office--one sans" style="font-style:normal">
    <div class="office__name"><svg width="8" height="11" viewBox="0 0 8 11" aria-hidden="true"><path d="M4 0a4 4 0 0 1 4 4c0 3-4 7-4 7S0 7 0 4a4 4 0 0 1 4-4z" fill="var(--teal)"/><circle cx="4" cy="4" r="1.5" fill="#fff"/></svg>Brookhaven Office</div>
    4800 Tillman Road,<br>Suite 1400, Charlotte,<br>NC 28219<br>&#9990; (704) 555-0187
  </address>
  <address class="abs office office--two sans" style="font-style:normal">
    <div class="office__name"><svg width="8" height="11" viewBox="0 0 8 11" aria-hidden="true"><path d="M4 0a4 4 0 0 1 4 4c0 3-4 7-4 7S0 7 0 4a4 4 0 0 1 4-4z" fill="var(--teal)"/><circle cx="4" cy="4" r="1.5" fill="#fff"/></svg>Whitcombe Office</div>
    13540 Quarry Lane,<br>Suite 300, Charlotte,<br>NC 28269<br>&#9990; (704) 555-0187
  </address>
  <div class="abs stamp"></div>
  <div class="abs address-line" style="top:230px"></div>
  <div class="abs address-line" style="top:273px"></div>
  <div class="abs address-line" style="top:316px"></div>
  <div class="abs address-line" style="top:359px"></div>
</section>

</body>
</html>
```